Business Card Design

I need a business card for my resume writing business. I have a logo that Im not keen on anymore so I would like the business card to use my photo instead of a logo. I am for mid career and trades resumes and prefer not to do executive resumes so don't need to aim for exectives. I would like it to be colourful. I like bright sky blue and maybe some pink or purple but primarily bright sky blue. I don't like green and Im keen see a fair bit of white on the card. As I have a photo to go it, it will need to go on a white background.

Target Market(s)

mid range careers. Not executives

Industry/Entity Type

Business

Contact Information for Business Card

Wyn Marchetti
Resume Writer
Clear Path CVs
27 The Lanyard
HARWOOD NSW 2465
wyn@clearpathcvs.com.au
0417362958
www.clearpathcvs.com.au

Requirements
Nice to have
• Maybe colours similar to my website - www.clearpathcvs.com.au but not with any black on it.
Should not have
• No green or dark colours

```html
<!DOCTYPE html>
<html lang="en">
<head>
<meta charset="utf-8">
<title>Clear Path CVs – Business Card</title>
<link rel="stylesheet" href="https://fonts.googleapis.com/css2?family=Lato:wght@400;700;900&display=swap">
<style>
  :root {
    --backdrop: #4a4a4a;
    --card-white: #ffffff;
    --sky: #29a8e0;
    --sky-deep: #1b86c6;
    --ink-blue: #1a74b0;
    --text-blue: #2a86c0;
  }
  * { box-sizing: border-box; margin: 0; padding: 0; }
  html, body {
    width: 1200px; height: 900px; overflow: hidden;
    background: var(--backdrop);
    font-family: "Lato", Arial, sans-serif;
  }
  .card {
    position: absolute; left: 100px; top: 145px;
    width: 1000px; height: 610px;
    background: var(--card-white);
    border-radius: 30px;
    overflow: hidden;
  }
  .card__accent-shape { position: absolute; inset: 0; width: 100%; height: 100%; }
  .name-marker {
    position: absolute; left: 0; top: 78px;
    width: 52px; height: 44px; background: var(--sky);
  }
  .holder-name {
    position: absolute; left: 72px; top: 68px;
    font-size: 56px; letter-spacing: 1px;
    color: var(--ink-blue); line-height: 1;
  }
  .holder-name__first { font-weight: 900; }
  .holder-name__last { font-weight: 400; }
  .contact-list {
    position: absolute; left: 72px; top: 172px;
    list-style: none;
  }
  .contact-list li {
    display: flex; align-items: center; gap: 14px;
    height: 40px;
    font-size: 26px; letter-spacing: 1.5px;
    color: var(--text-blue);
  }
  .contact-list svg { width: 26px; height: 26px; flex: none; }
  .business-name {
    position: absolute; left: 72px; top: 440px;
    font-size: 38px; font-weight: 700; color: var(--ink-blue);
  }
  .business-address {
    position: absolute; left: 72px; top: 498px;
    font-size: 24px; color: var(--text-blue); letter-spacing: 0.5px;
  }
  .portrait-frame {
    position: absolute; left: 655px; top: 185px;
    width: 232px; height: 226px;
    border: 9px solid var(--sky-deep);
    background: var(--card-white);
  }
  .portrait {
    width: 100%; height: 100%;
    background: radial-gradient(circle at 50% 45%, #c99b84 0%, #8a5a46 35%, #e9eef2 70%, #f5f7f9 100%);
  }
  .job-title {
    position: absolute; left: 655px; top: 430px; width: 232px;
    text-align: center;
    font-size: 22px; font-weight: 700; letter-spacing: 1px;
    color: var(--card-white);
  }
</style>
</head>
<body>
  <div class="card">
    <svg class="card__accent-shape" viewBox="0 0 1000 610" preserveAspectRatio="none" aria-hidden="true">
      <polygon points="810,0 1000,0 1000,610 610,610" fill="var(--sky)"/>
      <polygon points="790,0 814,0 614,610 590,610" fill="var(--sky-deep)"/>
      <polygon points="655,411 905,411 905,425 650,425" fill="var(--sky-deep)"/>
    </svg>

    <div class="name-marker"></div>
    <h1 class="holder-name"><span class="holder-name__first">WYN</span> <span class="holder-name__last">MARCHETTI</span></h1>

    <ul class="contact-list">
      <li>
        <svg viewBox="0 0 24 24"><path fill="var(--ink-blue)" d="M3 8c0-2 3-4 9-4s9 2 9 4v2h-5V8H8v2H3z M6 11h12l2 9H4z"/><circle cx="12" cy="15" r="2.4" fill="#fff"/></svg>
        <span>0417 36 29 58</span>
      </li>
      <li>
        <svg viewBox="0 0 24 24"><rect x="2" y="3" width="20" height="14" rx="1" fill="none" stroke="var(--ink-blue)" stroke-width="2.2"/><rect x="8" y="19" width="8" height="2.5" fill="var(--ink-blue)"/></svg>
        <span>clearpathcvs.com.au</span>
      </li>
      <li>
        <svg viewBox="0 0 24 24"><rect x="2" y="5" width="20" height="14" fill="var(--ink-blue)"/><path d="M2 5l10 8 10-8" fill="none" stroke="#fff" stroke-width="1.8"/></svg>
        <span>wyn@clearpathcvs.com.au</span>
      </li>
    </ul>

    <h2 class="business-name">Clear Path CVs</h2>
    <p class="business-address">27 The Lanyard HARWOOD NSW 2465</p>

    <div class="portrait-frame">
      <div class="portrait" role="img" aria-label="Portrait photo of Wyn Marchetti"></div>
    </div>
    <p class="job-title">RESUME WRITER</p>
  </div>
</body>
</html>
```